CD-/Plattencover für Debut Maxi-CD
Sehr unkomplizierter Ablauf mit KRIX. Sehr kooperaratives Eingehen auf Wünsche. Gerne wieder!
Zielgruppe
Instrumentale Hardrockband (3Celli+Drums).
Aufgabenstellung
Wir sind eine Instrumentale-Metal-Hardrockband aus Basel und suchen für unsere erste Studiomaxi ein vierseitiges Booklet inkl. CD-Cover und ein Disk-Cover.
Aufgabenstellung:
Front Cover: dunkel, mystisch, geheimnisvoll.
Bandname: GrimVortex, sowie Logo muss prominent verwendet, gerne eingearbeitet werden.
Titel: Tiefgang Vol.1 (nicht so wichtig wie Bandname/Logo)
2 Innenseiten mit div. Texten die wir noch bekanntgeben, und eine Rückseite mit den Song Titeln:
1. Rusty Kettle
2. Ohne Fritz
3. Cold Pickle
4. Gutwrench
5. Bonus: Odd as rain (Cover)
Disk-Cover kann wie CD Cover sein.

```html
<!DOCTYPE html>
<html lang="de">
<head>
<meta charset="utf-8">
<title>GrimVortex – Tiefgang Vol.1</title>
<link href="https://fonts.googleapis.com/css2?family=Bebas+Neue&display=swap" rel="stylesheet">
<style>
  :root {
    --stage: #5b5e5d;
    --paper: #141414;
    --paper-light: #2a2a2a;
    --ink: #f2f2f2;
    --silver: #d8d8d8;
    --silver-mid: #a9a9a9;
    --ember: #f08a24;
    --disc-rim: #9a9a9a;
    --disc-hub: #7d7d7d;
    --disc-hole: #5b5e5d;
  }
  * { box-sizing: border-box; margin: 0; padding: 0; }
  html, body {
    width: 1200px; height: 1200px; overflow: hidden;
    background: var(--stage);
    font-family: "Bebas Neue", "Oswald", sans-serif;
    color: var(--ink);
  }
  .canvas { position: relative; width: 1200px; height: 1200px; }

  .panel {
    position: absolute;
    background: radial-gradient(circle at 35% 30%, var(--paper-light) 0%, var(--paper) 70%);
    overflow: hidden;
  }
  .embers {
    position: absolute; inset: 0;
    background:
      radial-gradient(circle at 72% 68%, rgba(240,138,36,.35) 0 2px, transparent 3px),
      radial-gradient(circle at 80% 75%, rgba(240,138,36,.5) 0 2px, transparent 3px),
      radial-gradient(circle at 64% 80%, rgba(240,138,36,.4) 0 1.5px, transparent 3px),
      radial-gradient(circle at 88% 60%, rgba(240,138,36,.45) 0 2px, transparent 3px),
      radial-gradient(circle at 20% 88%, rgba(240,138,36,.35) 0 2px, transparent 3px);
  }
  .advisory-badge {
    position: absolute; top: 26px; right: 22px;
    width: 72px; height: 48px;
    background: var(--ink); padding: 3px;
  }
  .advisory-badge span { display: block; width: 100%; height: 100%; background: #000; }

  .artwork {
    position: absolute;
    background: radial-gradient(ellipse at 50% 45%, var(--silver) 0%, var(--silver-mid) 45%, rgba(60,60,60,0) 72%);
    border-radius: 45% 45% 30% 30%;
  }

  .band-name {
    position: absolute; left: 0; right: 0;
    text-align: center;
    color: var(--silver);
    letter-spacing: 2px;
    line-height: 1;
  }

  /* disc */
  .disc {
    position: absolute; left: 560px; top: 60px;
    width: 480px; height: 480px; border-radius: 50%;
    background: var(--disc-rim); padding: 12px;
  }
  .disc-face {
    position: relative; width: 100%; height: 100%; border-radius: 50%;
    overflow: hidden;
    background: radial-gradient(circle at 40% 35%, var(--paper-light), var(--paper) 70%);
  }
  .disc-face .artwork { left: 60px; top: 20px; width: 360px; height: 250px; }
  .disc-face .band-name { bottom: 62px; font-size: 62px; }
  .disc-hub {
    position: absolute; left: 50%; top: 50%;
    width: 150px; height: 150px; margin: -75px 0 0 -75px;
    border-radius: 50%; background: var(--disc-hub);
    display: flex; align-items: center; justify-content: center;
  }
  .disc-hub span { width: 56px; height: 56px; border-radius: 50%; background: var(--disc-hole); }

  /* front cover */
  .front-cover { left: 160px; top: 50px; width: 500px; height: 500px; box-shadow: 6px 6px 18px rgba(0,0,0,.4); }
  .front-cover .artwork { left: 70px; top: 70px; width: 360px; height: 260px; }
  .front-cover .band-name { top: 335px; font-size: 76px; }
  .front-cover .album-title {
    position: absolute; left: 0; right: 0; bottom: 48px;
    text-align: center; font-size: 34px; letter-spacing: 1px; line-height: 1;
  }

  /* booklet */
  .back-cover { left: 50px; top: 640px; width: 340px; height: 340px; }
  .tracklist { list-style: none; position: absolute; left: 32px; top: 90px; }
  .tracklist li { font-size: 24px; line-height: 33px; letter-spacing: .5px; }

  .inner-page { top: 640px; width: 370px; height: 340px; padding: 30px 30px; display: flex; align-items: center; }
  .inner-left { left: 410px; }
  .inner-right { left: 780px; border-left: 1px solid #000; }
  .inner-page p { font-size: 18px; line-height: 22px; text-align: center; letter-spacing: .3px; }
</style>
</head>
<body>
<div class="canvas">

  <div class="disc">
    <div class="disc-face">
      <div class="artwork" role="img" aria-label="Platz für die Cover-Illustration in Silber- und Grautönen"></div>
      <div class="disc-hub"><span></span></div>
      <div class="band-name">GrimVortex</div>
    </div>
  </div>

  <section class="panel front-cover">
    <div class="embers"></div>
    <div class="advisory-badge"><span></span></div>
    <div class="artwork" role="img" aria-label="Platz für die Cover-Illustration in Silber- und Grautönen"></div>
    <div class="band-name">GrimVortex</div>
    <div class="album-title">Tiefgang Vol.1</div>
  </section>

  <section class="panel back-cover">
    <div class="embers"></div>
    <ol class="tracklist">
      <li>1. Rusty Kettle</li>
      <li>2. Ohne Fritz</li>
      <li>3. Cold Pickle</li>
      <li>4. Gutwrench</li>
      <li>5. Bonus: Odd as rain (Cover)</li>
    </ol>
  </section>

  <section class="panel inner-page inner-left">
    <p>Lorem ipsum dolor sit amet, consectetuer adipiscing elit. Aenean commodo ligula eget dolor. Aenean massa. Cum sociis natoque penatibus et magnis dis parturient montes, nascetur ridiculus mus. Donec quam felis, ultricies nec, pellentesque eu, pretium quis, sem. Nulla consequat massa quis enim. Donec pede justo, fringilla vel, aliquet nec, vulputate eget, arcu. In enim justo, rhoncus ut, imperdiet a, venenatis vitae, justo. Nullam dictum felis eu pede mollis pretium. Integer tincidunt.</p>
  </section>

  <section class="panel inner-page inner-right">
    <p>Lorem ipsum dolor sit amet, consectetuer adipiscing elit. Aenean commodo ligula eget dolor. Aenean massa. Cum sociis natoque penatibus et magnis dis parturient montes, nascetur ridiculus mus. Donec quam felis, ultricies nec, pellentesque eu, pretium quis, sem. Nulla consequat massa quis enim. Donec pede justo, fringilla vel, aliquet nec, vulputate eget, arcu. In enim justo, rhoncus ut, imperdiet a, venenatis vitae, justo. Nullam dictum felis eu pede mollis pretium. Integer tincidunt.</p>
  </section>

</div>
</body>
</html>
```